Consulting company with focus on aviation needs

We need a new business card design for our company. The company consults with multiple players in the industry like manufacturers and airlines. It is also a supplier and an inter-company level. Given the targeted industry (aviation) it should be both kind of serious, sound, secure, classy, ​​but also a bit technical, innovative. Should not be too playful, however, "fresh", "airy", "ligth" and "suprising" are suitabe attributes. The existing logo shall be used.

Airlines

```html
<!DOCTYPE html>
<html lang="en">
<head>
<meta charset="utf-8">
<title>Aerolis Business Card</title>
<link href="https://fonts.googleapis.com/css2?family=Questrial&display=swap" rel="stylesheet">
<style>
  :root {
    --backdrop: #3b2c22;
    --card: #ffffff;
    --card-shade: #f3f3f3;
    --ink: #3f3f3f;
    --wordmark: #555a5c;
    --accent-orange: #f0962a;
    --accent-teal: #1f9a85;
    --accent-green: #8cb84a;
    --halo: #eef1ef;
  }
  * { margin: 0; padding: 0; box-sizing: border-box; }
  html, body { width: 1200px; height: 960px; overflow: hidden; }
  body {
    background: var(--backdrop);
    font-family: "Questrial", sans-serif;
    position: relative;
  }
  .card {
    position: absolute;
    top: 339px;
    width: 514px;
    height: 290px;
    border-radius: 10px;
    background: linear-gradient(180deg, var(--card) 60%, var(--card-shade) 100%);
    overflow: hidden;
  }
  .card--front { left: 78px; }
  .card--back { left: 608px; }
  .halo {
    position: absolute;
    width: 304px;
    height: 304px;
    border-radius: 50%;
    background: var(--halo);
  }
  .card--front .halo { left: 370px; top: -7px; }
  .card--back .halo { left: -160px; top: -7px; }
  .brand {
    position: absolute;
    text-align: center;
  }
  .brand-dot {
    width: 48px; height: 48px;
    border-radius: 50%;
    background: var(--accent-teal);
    margin: 0 auto 10px;
  }
  .brand-name {
    font-size: 28px;
    letter-spacing: 4px;
    color: var(--wordmark);
    line-height: 1;
  }
  .brand-tagline {
    font-size: 9px;
    color: var(--accent-orange);
    margin-top: 5px;
    white-space: nowrap;
  }
  .card--front .brand { left: 30px; top: 36px; width: 150px; }
  .card--back .brand { left: 322px; top: 162px; width: 150px; }
  .person {
    position: absolute;
    left: 34px;
    top: 150px;
  }
  .person-name { font-size: 21px; color: var(--accent-orange); line-height: 1.1; }
  .person-role { font-size: 13px; color: var(--ink); margin-top: 1px; }
  .contacts {
    position: absolute;
    left: 34px;
    top: 198px;
    list-style: none;
  }
  .contacts li {
    display: flex;
    align-items: center;
    gap: 6px;
    font-size: 11.5px;
    color: var(--ink);
    height: 17px;
  }
  .contacts svg { width: 11px; height: 11px; flex: none; }
</style>
</head>
<body>
  <section class="card card--front">
    <div class="halo"></div>
    <div class="brand">
      <div class="brand-dot"></div>
      <div class="brand-name">AEROLIS</div>
      <div class="brand-tagline">Linking Partners - Shaping Insight</div>
    </div>
    <div class="person">
      <div class="person-name">Daniel Hart</div>
      <div class="person-role">President</div>
    </div>
    <ul class="contacts">
      <li>
        <svg viewBox="0 0 12 12"><path d="M2.5 1 L4.5 1 L5 3.5 L3.8 4.5 Q5 7 7.5 8.2 L8.5 7 L11 7.5 L11 9.5 Q10 11 8 11 Q1 9 1 2.5 Q1 1.2 2.5 1 Z" fill="var(--accent-teal)"/></svg>
        555 014 2290
      </li>
      <li>
        <svg viewBox="0 0 12 12"><rect x="3" y="0.8" width="6" height="10.4" rx="1" fill="none" stroke="var(--accent-green)" stroke-width="1.3"/><circle cx="6" cy="9.3" r="0.7" fill="var(--accent-green)"/></svg>
        555 017 4836
      </li>
      <li>
        <svg viewBox="0 0 12 12"><rect x="0.5" y="2.5" width="11" height="7.5" rx="0.8" fill="var(--accent-orange)"/><path d="M0.8 3 L6 7 L11.2 3" fill="none" stroke="#fff" stroke-width="1"/></svg>
        info@skylinecounsel.net
      </li>
      <li>
        <svg viewBox="0 0 12 12"><circle cx="6" cy="6" r="5" fill="none" stroke="#777" stroke-width="1"/><ellipse cx="6" cy="6" rx="2.2" ry="5" fill="none" stroke="#777" stroke-width="0.9"/><path d="M1 6 H11 M2 3.5 H10 M2 8.5 H10" stroke="#777" stroke-width="0.8"/></svg>
        www.skylinecounsel.net
      </li>
    </ul>
  </section>

  <section class="card card--back">
    <div class="halo"></div>
    <div class="brand">
      <div class="brand-dot"></div>
      <div class="brand-name">AEROLIS</div>
      <div class="brand-tagline">Linking Partners - Shaping Insight</div>
    </div>
  </section>
</body>
</html>
```